Halt and Thicken New Branding Stationary Set - updated Oct 30th 2017

Updated on 30th Oct 2017 as we now need a whole folder design instead of a folder cover. We have thought out exactly what should be on it so it wont be hard. We are happy for this to be completed only by the winning designer if you like. And also we are guaranteeing this project now. Thanks!

We just got our new logo and now we would like a stationary set so we can brand our company communications. The items we need designed are:
Business cards
Letterhead
Appointment confirmation cards
Folder - switched from folder cover. Note that if you don't wish to do this unless you are selected as the winner this is fine.

1. Business cards - for 5 employees, final names will be given once the winner is selected, but you can use this one as the sample:
Lucinda Prieto
Hair Regrowth Expert
Halt and Thicken
7127 Marbury Ave, Suite 500
Kestrel Park CA 90877
lucinda@gavinthorpemd.example
(555) 238-9016

2. Letterhead 8.5" x 11.0" vertical
Halt and Thicken
Kestrel Park CA 90877
office@haltandthicken.example
(555) 238-9016

3. Appointment Confirmation cards - business card size
Halt and Thicken
Kestrel Park CA 90877
Appointment For:
Date:
Time:
If you are unable to make your appointment, please contact us to reschedule at:
(555) 238-9016
info@gavinthorpemd.example

*UPDATED*
4. Folder 9" x 12 " vertical with double pocket
We would like the infinity image from the logo made really big so the left side is on the back and the right side with the + sign is on the front and its takes up the maximum room on the folder.
On the front below the half logo it should say "A Biochemical Revolution..."
On the inside we would also like to have the infinity sign from the logo but faded and half on the left pocket half on the right.
On left inside pocket it should say (this will be partically written on top of the logo):
Gavin Thorpe MD
Precision Medicine
Halt and Thicken Hair
On the Right inside pocket it should say the following:
Because the Enemy of BETTER Health is Good Health
BETTER Ingredients
BETTER Recipe
BETTER Medicine
On the back below the logo on the bottom should be the contact information.
I attached a picture of our drawing of what we want for this to make it easier.

Here is our website to give you an idea of our branding: http://www.haltandthicken.example/

We are the only true cure for hair loss and need to look professional and highest quality and beyond reproach from an ethical standpoint. We are a medical clinic so this should be portrayed also.
We cured hair loss by analyzing biochemistry and rebalancing it so that the process reverses and your own hair can grow back naturally.

Business card information:

OK so here is the information for the business cards:

Lucinda Prieto
Hair Regrowth Expert
(555) 238-9016
www.haltandthicken.example

Marisol Quintero
Hair Growth Consultant
(555) 238-9016
marisol@gavinthorpemd.example
www.haltandthicken.example

Glenda Hutchins
CMO/COO
(555) 238-9016
glenda@haltandthicken.example
www.haltandthicken.example

Dr Lou Thorpe
President
(555) 238-9016
info@gavinthorpemd.example
www.haltandthicken.example

Halt and Thicken
Customer Service
(555) 238-9016
info@gavinthorpemd.example
www.haltandthicken.example

Target Market(s)

Men aged 20-24 who care about their appearance, care about their hair and care about the world.

Industry/Entity Type

Medical And Science

Font styles to use
Sans Serif

Colors
00a990
ffffff
9d9d9d
333333

Requirements
Must have
• Must use the logo and our brand colors from the logo in all designs.
• The pantone colors are:
• Green: #4ca26f
• Light Grey: #999999
• The design should be symmetrical and balanced.
Nice to have
• It should look reasonably masculine.
Should not have
• Do not include any red in the design.

```html
<!DOCTYPE html>
<html lang="en">
<head>
<meta charset="utf-8">
<title>Halt and Thicken — Business Card</title>
<link rel="stylesheet" href="https://fonts.googleapis.com/css2?family=Roboto+Condensed:wght@400;700&family=Open+Sans:wght@400&display=swap">
<style>
  :root {
    --stage: #0d0a2c;
    --paper: #ffffff;
    --brand-green: #48d84a;
    --ink: #3a3f4a;
    --ink-grey: #8f9596;
  }
  * { margin: 0; padding: 0; box-sizing: border-box; }
  html, body { width: 1171px; height: 1200px; overflow: hidden; background: var(--stage); }
  .canvas { position: relative; width: 1171px; height: 1200px; }

  .card { position: absolute; left: 231px; width: 710px; height: 405px; overflow: hidden; }
  .card-front { top: 158px; background: var(--paper); font-family: "Roboto Condensed", Arial, sans-serif; }
  .card-back { top: 638px; background: var(--brand-green); font-family: "Open Sans", Arial, sans-serif; }

  .brand-lockup { position: absolute; left: 56px; top: 62px; display: flex; align-items: center; gap: 12px; }
  .brand-mark { width: 22px; height: 22px; background: var(--brand-green); }
  .brand-name { font-weight: 700; font-size: 27px; color: var(--brand-green); letter-spacing: 0.5px; }

  .identity { position: absolute; right: 51px; top: 46px; text-align: right; }
  .person-name { font-weight: 700; font-size: 31px; color: var(--brand-green); letter-spacing: 0.5px; line-height: 36px; }
  .person-role { font-weight: 700; font-size: 15px; color: var(--ink); margin-top: 2px; }
  .company { font-weight: 700; font-size: 21px; color: var(--brand-green); margin-top: 50px; line-height: 26px; }
  .address-line { font-weight: 700; font-size: 19px; color: var(--ink); line-height: 26px; }

  .contacts { position: absolute; left: 48px; top: 226px; list-style: none; }
  .contact { display: flex; align-items: center; gap: 12px; height: 33px; font-weight: 700; font-size: 20px; color: var(--ink); }
  .contact-icon { width: 22px; height: 22px; flex: none; }

  .footer-band { position: absolute; left: 0; right: 0; bottom: 0; height: 23px; background: var(--brand-green); }

  .back-lockup { position: absolute; left: 0; right: 0; top: 150px; text-align: center; }
  .back-name { display: inline-flex; align-items: center; gap: 12px; font-family: "Roboto Condensed", Arial, sans-serif; font-weight: 700; font-size: 34px; color: var(--paper); letter-spacing: 0.5px; }
  .back-mark { width: 24px; height: 24px; background: var(--paper); }
  .back-url { position: absolute; left: 0; right: 0; top: 234px; text-align: center; font-size: 23px; color: var(--paper); }
</style>
</head>
<body>
<main class="canvas">
  <section class="card card-front">
    <div class="brand-lockup">
      <span class="brand-mark"></span>
      <span class="brand-name">HALT AND THICKEN</span>
    </div>

    <div class="identity">
      <p class="person-name">LUCINDA PRIETO</p>
      <p class="person-role">Hair Regrowth Expert</p>
      <p class="company">Halt and Thicken</p>
      <p class="address-line">7127 Marbury Ave, Suite 500</p>
      <p class="address-line">Kestrel Park CA 90877</p>
    </div>

    <ul class="contacts">
      <li class="contact">
        <svg class="contact-icon" viewBox="0 0 22 22" aria-hidden="true">
          <circle cx="11" cy="11" r="11" fill="var(--brand-green)"/>
          <rect x="7.5" y="5" width="7" height="12" rx="1.2" fill="none" stroke="#fff" stroke-width="1.6"/>
          <rect x="9" y="7" width="4" height="6" fill="#fff"/>
        </svg>
        (555) 238-9016
      </li>
      <li class="contact">
        <svg class="contact-icon" viewBox="0 0 22 22" aria-hidden="true">
          <circle cx="11" cy="11" r="11" fill="var(--brand-green)"/>
          <rect x="5.5" y="7" width="11" height="8" fill="none" stroke="#fff" stroke-width="1.5"/>
          <path d="M5.5 7 L11 11.5 L16.5 7" fill="none" stroke="#fff" stroke-width="1.5"/>
        </svg>
        lucinda@gavinthorpemd.example
      </li>
      <li class="contact">
        <svg class="contact-icon" viewBox="0 0 22 22" aria-hidden="true">
          <circle cx="11" cy="11" r="11" fill="var(--brand-green)"/>
          <circle cx="11" cy="11" r="6" fill="none" stroke="#fff" stroke-width="1.4"/>
          <ellipse cx="11" cy="11" rx="2.6" ry="6" fill="none" stroke="#fff" stroke-width="1.2"/>
          <line x1="5" y1="11" x2="17" y2="11" stroke="#fff" stroke-width="1.2"/>
        </svg>
        www.haltandthicken.example
      </li>
    </ul>

    <div class="footer-band"></div>
  </section>

  <section class="card card-back">
    <div class="back-lockup">
      <span class="back-name"><span class="back-mark"></span>HALT AND THICKEN</span>
    </div>
    <p class="back-url">www.haltandthicken.example</p>
  </section>
</main>
</body>
</html>
```